Business Card Upgrade

I have designed our business card using our new logo. I think it needs imporovements. We used to have two cards for our business. One card was for our software business, and the other was for our consulting business. We are now in the process of combining our websites, marketing, name, and a new logo.

Our goal is to have a really sharp professional logo. One reason I designed the card the way I did was that our Titles are sometimes long, and by separating the person's name and title, it shows up very well and the title can be adjusted no matter how long it is. Sometimes the title can be 4 or 5 words or more.

We really like our logo on black as it shows up very nice. Our PMS colors are as follows: 368C and 459C.

The Designer that will be working with us will need to deliver the following:

The front and back of the Business Card Design will need to be delivered in a high quality JPEG, and
The front and back of the Business Card Design in Illustrator Format .ai
Any fonts will need to be sent to us if they are not standard and are required to open the Illustrator file correctly.

To help us get a good idea of the card with a title, please use the title: " Director of Software Development "

NOTE: The chosen designer will be selected to design our new letterhead within 2 weeks from the closing of this contest.
Updates

To help us make sure the card design works with longer titles, please use the followign job title on the card:  

"Director of Software and Product Development"

 

ALL DESIGNERS:

1. I appreciate the different angles you are showing the cards, but please be sure and always show the direct view, so I can see the layout and what the person I hand the card will see.

2. Please do not use white.  Please use off white as I don't care for white cards and they get dirty easy and do not represent the designs well.

Dear Designers,

Please provide samples straight one as a viewer of the card will see.  Some of the angles that are presented make it impossible to tell how everything fits, and sometimes even makes areas look skewed. So, please provide a straight sample view.

Target Market(s)

Keystone 400 company executives such as Vice Presidents, and Directors

Industry/Entity Type

Software

Requirements
Must have
• Professional looking Card.

Our customers are Directors, Vice Presidents, and Presidents of companies as large as Keystone 400 companies. The card needs to get attention wile still looking professional.

Delivery of the finished product in Illustrator Format with any fonts needed to edit the text or open the file.

The card will be a heavy stock with a soft touch coating for that silk feel.

```html
<!DOCTYPE html>
<html lang="en">
<head>
<meta charset="utf-8">
<title>Meridian Trade Corporation – Business Card</title>
<link href="https://fonts.googleapis.com/css2?family=Arimo:wght@700&family=Roboto+Condensed:wght@400;700&display=swap" rel="stylesheet">
<style>
  :root {
    --page: #ffffff;
    --card-black: #000000;
    --card-charcoal: #3a3a3a;
    --brand-green: #5ba746;
    --brand-gold: #e3d08a;
    --gold-text: #e6d48f;
    --ink: #111111;
  }
  html, body {
    margin: 0;
    padding: 0;
    width: 1017px;
    height: 1200px;
    overflow: hidden;
    background: var(--page);
  }
  .sheet {
    position: relative;
    width: 1017px;
    height: 1200px;
  }
  .card {
    position: absolute;
    left: 150px;
    width: 722px;
    height: 401px;
    overflow: hidden;
  }
  .card--front {
    top: 146px;
    background: radial-gradient(ellipse 60% 62% at 50% 48%, var(--card-charcoal) 0%, #1c1c1c 55%, var(--card-black) 100%);
  }
  .card--back {
    top: 655px;
    background: var(--brand-gold);
  }
  .brand-name {
    position: absolute;
    font-family: "Roboto Condensed", sans-serif;
    font-weight: 700;
    color: var(--brand-green);
    text-transform: uppercase;
    line-height: 1;
    margin: 0;
  }
  .card--front .brand-name {
    left: 0;
    right: 0;
    top: 152px;
    text-align: center;
    font-size: 48px;
    letter-spacing: 3px;
  }
  .card--front .brand-name span {
    display: block;
    font-size: 25px;
    letter-spacing: 9px;
    margin-top: 10px;
  }
  .back-panel {
    position: absolute;
    left: 0;
    top: 0;
    width: 722px;
    height: 401px;
  }
  .card--back .brand-name {
    left: 39px;
    top: 50px;
    width: 230px;
    font-size: 36px;
    letter-spacing: 2px;
  }
  .card--back .brand-name span {
    display: block;
    font-size: 15px;
    letter-spacing: 3px;
    margin-top: 8px;
    white-space: nowrap;
  }
  .contact {
    position: absolute;
    left: 39px;
    top: 220px;
    margin: 0;
    font-family: "Roboto Condensed", sans-serif;
    font-style: normal;
    font-size: 19px;
    line-height: 24px;
    color: var(--gold-text);
  }
  .tagline {
    position: absolute;
    left: 318px;
    top: 70px;
    margin: 0;
    font-family: "Roboto Condensed", sans-serif;
    font-size: 20px;
    line-height: 25px;
    text-transform: uppercase;
    color: var(--ink);
  }
  .person-name {
    position: absolute;
    left: 315px;
    top: 232px;
    margin: 0;
    font-family: "Arimo", sans-serif;
    font-weight: 700;
    font-size: 46px;
    line-height: 1;
    color: var(--ink);
  }
  .person-title {
    position: absolute;
    left: 318px;
    top: 285px;
    margin: 0;
    font-family: "Roboto Condensed", sans-serif;
    font-size: 20px;
    line-height: 24px;
    color: var(--ink);
  }
</style>
</head>
<body>
<main class="sheet">
  <section class="card card--front" aria-label="Card front">
    <p class="brand-name">Meridian<span>Trade Corporation</span></p>
  </section>

  <section class="card card--back" aria-label="Card back">
    <svg class="back-panel" width="722" height="401" viewBox="0 0 722 401" aria-hidden="true">
      <path d="M0 0 H290 C300 40 310 80 302 140 C294 200 280 250 284 300 C287 345 296 375 298 401 H0 Z" fill="var(--card-black)"/>
    </svg>
    <p class="brand-name">Meridian<span>Trade Corporation</span></p>
    <address class="contact">
      418 Harbor Point Drive<br>
      Mobile, AL 36604<br>
      251.555.0148 (Direct)<br>
      dwhitman@meridiantrade.com<br>
      www.meridiantrade.com
    </address>
    <p class="tagline">The only firm with enough expertise<br>to offer every FTZ solution</p>
    <h1 class="person-name">Dale Whitman</h1>
    <p class="person-title">Director of Software and<br>Product Development</p>
  </section>
</main>
</body>
</html>
```